ORBITRIX LASER TAG

We require signage for the exterior of a building. The sign should be two lines of text

ORBITRIX
LASER TAG

the Orbitrix should be channel letters and larger than the sub text.

The signage is for the exterior of a building.

I have a draft from the sign builders that needs improvement. we must be futuristic and cool.

Industry/Entity Type

Building

Requirements
Must have
• TEXT ONLY VECTOR DESIGN ON COMPLETION

```html
<!DOCTYPE html>
<html lang="en">
<head>
<meta charset="utf-8">
<title>Orbitrix Laser Tag – Exterior Sign</title>
<link rel="stylesheet" href="https://fonts.googleapis.com/css2?family=Audiowide&display=swap">
<style>
  :root {
    --page-bg: #e9ebef;
    --panel-deep: #0b0f4a;
    --panel-mid: #17209a;
    --panel-edge: #0a0d3c;
    --neon-green: #39f23a;
    --neon-magenta: #ff3df0;
  }
  * { margin: 0; padding: 0; box-sizing: border-box; }
  html, body {
    width: 1200px;
    height: 1000px;
    overflow: hidden;
    background: var(--page-bg);
  }
  .canvas {
    position: relative;
    width: 1200px;
    height: 1000px;
  }
  .sign {
    position: absolute;
    left: 50px;
    top: 391px;
    width: 1100px;
    height: 218px;
    overflow: hidden;
    box-shadow: 0 10px 30px rgba(10, 13, 60, 0.25);
  }
  .sign-backdrop {
    position: absolute;
    inset: 0;
    background:
      radial-gradient(ellipse at 30% 50%, var(--panel-mid) 0%, var(--panel-deep) 60%, var(--panel-edge) 100%);
  }
  .sign-title {
    position: absolute;
    right: 12px;
    top: 12px;
    font-family: "Audiowide", sans-serif;
    font-size: 112px;
    font-weight: 400;
    line-height: 1;
    letter-spacing: 4px;
    color: var(--neon-green);
    white-space: nowrap;
  }
  .sign-subtitle {
    position: absolute;
    right: 14px;
    top: 132px;
    font-family: "Audiowide", sans-serif;
    font-size: 66px;
    line-height: 1;
    letter-spacing: 3px;
    color: var(--neon-magenta);
    white-space: nowrap;
  }
</style>
</head>
<body>
  <main class="canvas">
    <section class="sign" aria-label="Orbitrix Laser Tag exterior sign">
      <div class="sign-backdrop" role="img" aria-label="Deep navy starfield background"></div>
      <h1 class="sign-title">ORBITRIX</h1>
      <p class="sign-subtitle">LASER TAG</p>
    </section>
  </main>
</body>
</html>
```